Business card for Luxury Portable Restroom Trailer company

We are a Luxury Portable Restroom Trailer Company Called PELIKAR HIRES. Based in Orange County California. We provide portable restroom trailers for events, such as, Weddings, Concerts, Charity events, Sporting events, Tournaments, Corporate events, ect. We rent and Sell the Luxury restrooms. Our colors are white, grey, and Orange. As you will see in the logo we uploaded.
There are 2 people in the company so the names and titles will change for the 3 people but card will remain the same. Here is the information for each Person: Dennis Moyle CFO 555 018-3647
next Person: Wesley Tanford VP 555 018-3647
Next Person: Miles Tanford CEO 555 018-3647
Information to include on the card: Luxury Restroom Trailers Rental and Sales. Weddings, Concerts, Charity, Sporting and Corp. Events.

```html
<!DOCTYPE html>
<html lang="en">
<head>
<meta charset="utf-8">
<title>Pelikar Hires – Business Card</title>
<link href="https://fonts.googleapis.com/css2?family=Lato:wght@400;700;900&display=swap" rel="stylesheet">
<style>
  :root {
    --orange: #e8662a;
    --orange-deep: #d95d22;
    --grey: #555658;
    --grey-light: #7a7b7d;
    --white: #ffffff;
    --backdrop: #2b2c2e;
  }
  * { box-sizing: border-box; margin: 0; padding: 0; }
  html, body {
    width: 1200px;
    height: 900px;
    overflow: hidden;
    background: var(--backdrop);
    font-family: "Lato", sans-serif;
  }
  .sheet {
    width: 1200px;
    height: 900px;
    display: flex;
    flex-direction: column;
    align-items: center;
    justify-content: center;
    gap: 60px;
  }
  .card {
    position: relative;
    width: 560px;
    height: 320px;
    border-radius: 28px;
    overflow: hidden;
  }
  .card--front {
    background: linear-gradient(100deg, var(--orange-deep), var(--orange));
    display: flex;
    align-items: center;
    justify-content: center;
  }
  .wordmark {
    font-weight: 900;
    font-size: 46px;
    letter-spacing: 2px;
    line-height: 1;
    text-align: center;
  }
  .wordmark--light { color: var(--white); }
  .wordmark--dark { color: var(--grey); }

  .card--back {
    background: var(--white);
  }
  .holder {
    position: absolute;
    top: 38px;
    left: 40px;
  }
  .holder__line {
    display: flex;
    align-items: baseline;
    gap: 8px;
  }
  .holder__name {
    color: var(--orange);
    font-weight: 700;
    font-size: 19px;
    text-transform: uppercase;
    letter-spacing: 0.5px;
  }
  .holder__divider { color: var(--orange); font-size: 19px; }
  .holder__title {
    color: var(--grey);
    font-size: 18px;
    letter-spacing: 0.5px;
  }
  .holder__phone {
    display: flex;
    align-items: center;
    gap: 8px;
    margin-top: 8px;
    color: var(--grey);
    font-size: 16px;
  }
  .card--back .wordmark {
    position: absolute;
    top: 128px;
    left: 0;
    right: 0;
    font-size: 40px;
  }
  .services {
    position: absolute;
    right: 36px;
    bottom: 40px;
    text-align: right;
  }
  .services__heading {
    display: flex;
    align-items: center;
    justify-content: flex-end;
    gap: 10px;
    color: var(--orange);
    font-weight: 700;
    font-size: 17px;
    letter-spacing: 0.5px;
    margin-bottom: 6px;
  }
  .services__rule {
    width: 170px;
    height: 1.5px;
    background: var(--orange);
  }
  .services__line {
    color: var(--grey);
    font-size: 14.5px;
    line-height: 1.45;
  }
</style>
</head>
<body>
  <main class="sheet">
    <section class="card card--front" aria-label="Card front">
      <div class="wordmark wordmark--light">PELIKAR HIRES</div>
    </section>

    <section class="card card--back" aria-label="Card back">
      <div class="holder">
        <div class="holder__line">
          <span class="holder__name">Dennis Moyle</span>
          <span class="holder__divider">|</span>
          <span class="holder__title">CFO</span>
        </div>
        <div class="holder__phone">
          <svg width="10" height="16" viewBox="0 0 10 16" aria-hidden="true">
            <rect x="1" y="1" width="8" height="14" rx="1.5" fill="none" stroke="var(--orange)" stroke-width="1.4"/>
            <line x1="4" y1="12.5" x2="6" y2="12.5" stroke="var(--orange)" stroke-width="1.2"/>
          </svg>
          <span>555 018-3647</span>
        </div>
      </div>

      <div class="wordmark wordmark--dark">PELIKAR HIRES</div>

      <div class="services">
        <div class="services__heading">
          <span class="services__rule"></span>
          <span>OUR SERVICES</span>
        </div>
        <p class="services__line">Luxury Restroom Trailers Rental and Sales</p>
        <p class="services__line">Weddings, Concerts, Charity, Sporting and Corp. Events.</p>
      </div>
    </section>
  </main>
</body>
</html>
```